New Jar Label for Manuka Honey Company!

Hine Roa Honey, a Manuka Honey company from New Zealand is looking for a fresh & engaging label for our manuka honey jars.

Attached are some examples of label designs that we like, feel free to use the language/copy on these labels for inspiration/content/copy, but feel free to add your own creative spin if you have a great design idea!

LABEL DIMENSIONS: 1654mmx532mm

Label Must Include:
- MGO rating
- Made (or) Product of New Zealand
- Manuka Honey (can add extra text similar to attached examples)

Label Can Include:
- Badges: raw food, non gmo, bpa free, gluten free, halal etc
- anything you feel is appropriate

You can change the color of the logo(s) to Black, White, Silver or Gold.

Can you please include a mockup of your label design(s) on the supplied "Jar Mockup File". You can change the scene of the mockup if you like.

UPDATE:

Have decided on bee logo so please bo longer use the mountain logo for label mockups. Design(s) will need multiple color variations to represent the other MGO ratings, flavor combos and other honey types, other than manuka.

• Provide multiple designs for each honey type
Manuka Design
Spring Honey Design
MGO 100-1000 Design(s)
Wildflower Honey Design
Flavor Combo Honey Design

```html
<!DOCTYPE html>
<html lang="en">
<head>
<meta charset="utf-8">
<title>Hine Roa Honey – Manuka Honey Label</title>
<link rel="stylesheet" href="https://fonts.googleapis.com/css2?family=Comfortaa:wght@300;400&family=Montserrat:wght@400;500;600&display=swap">
<style>
  :root {
    --backdrop: #6f979d;
    --label-white: #ffffff;
    --band-light: #d6f0f4;
    --band-mid: #c4e8ef;
    --badge-blue: #cdeef3;
    --honey-gold: #ddae1e;
    --honey-gold-light: #e6c04a;
    --seal-cream: #f3e3a6;
    --rating-cream: #fbf3df;
    --ink: #2f3a40;
    --rule: #8a8a8a;
    --on-gold: #ffffff;
  }
  html, body {
    margin: 0;
    padding: 0;
    width: 1200px;
    height: 824px;
    overflow: hidden;
    background: var(--backdrop);
  }
  .canvas {
    position: relative;
    width: 1200px;
    height: 824px;
    overflow: hidden;
    background: var(--backdrop);
  }
  .jar-label {
    position: absolute;
    left: 120px;
    top: 122px;
    width: 960px;
    height: 580px;
    background: var(--label-white);
    box-shadow: 0 12px 30px rgba(0,0,0,0.18);
  }
  .jar-label svg { display: block; }
  .brand-name {
    font-family: "Montserrat", sans-serif;
    font-weight: 500;
    font-size: 22px;
    letter-spacing: 4px;
    fill: var(--ink);
  }
  .origin {
    font-family: "Montserrat", sans-serif;
    font-weight: 600;
    font-size: 12.5px;
    fill: var(--on-gold);
  }
  .product-name {
    font-family: "Comfortaa", sans-serif;
    font-weight: 300;
    font-size: 46px;
    fill: var(--on-gold);
  }
  .mgo-grade {
    font-family: "Montserrat", sans-serif;
    font-weight: 400;
    font-size: 19px;
    fill: var(--on-gold);
  }
  .rating-value {
    font-family: "Montserrat", sans-serif;
    font-weight: 400;
    font-size: 13px;
    letter-spacing: 9px;
    fill: var(--ink);
  }
  .net-weight {
    font-family: "Montserrat", sans-serif;
    font-weight: 600;
    font-size: 6px;
    fill: var(--ink);
  }
</style>
</head>
<body>
<main class="canvas">
  <section class="jar-label">
    <svg width="960" height="580" viewBox="0 0 960 580" xmlns="http://www.w3.org/2000/svg">
      <defs>
        <linearGradient id="bandTone" x1="0" x2="1" y1="0" y2="0">
          <stop offset="0" stop-color="var(--band-mid)"/>
          <stop offset="0.5" stop-color="var(--band-light)"/>
          <stop offset="1" stop-color="var(--band-mid)"/>
        </linearGradient>
        <linearGradient id="honeyTone" x1="0" x2="1" y1="0" y2="0">
          <stop offset="0" stop-color="var(--honey-gold-light)"/>
          <stop offset="0.35" stop-color="var(--honey-gold)"/>
          <stop offset="1" stop-color="var(--honey-gold)"/>
        </linearGradient>
      </defs>

      <!-- top band -->
      <rect class="honeycomb-band" x="0" y="0" width="960" height="95" fill="url(#bandTone)" role="img" aria-label="Pale blue honeycomb pattern band"/>

      <!-- brand -->
      <circle class="brand-dot" cx="350" cy="46" r="12" fill="var(--ink)"/>
      <text class="brand-name" x="378" y="54">HINE ROA HONEY CO.</text>

      <!-- honey drop -->
      <path class="honey-drop" d="M471,149 C565,149 652,232 641,320 C631,398 561,432 490,427 C400,421 330,370 335,288 C340,208 400,149 471,149 Z" fill="url(#honeyTone)"/>

      <!-- badges -->
      <circle class="badge" cx="318" cy="227" r="23" fill="var(--badge-blue)"/>
      <circle class="badge" cx="311" cy="284" r="23" fill="var(--badge-blue)"/>
      <circle class="badge" cx="335" cy="334" r="23" fill="var(--badge-blue)"/>

      <!-- seal -->
      <circle class="seal" cx="640" cy="287" r="40" fill="var(--seal-cream)" opacity="0.55" stroke="var(--badge-blue)" stroke-width="2"/>

      <text class="origin" x="479" y="236" text-anchor="middle">Product of New Zealand</text>
      <text class="product-name" x="371" y="287">manuka</text>
      <text class="product-name" x="371" y="329">honey</text>
      <line class="mgo-divider" x1="451" y1="373" x2="451" y2="403" stroke="var(--badge-blue)" stroke-width="2.5"/>
      <text class="mgo-grade" x="469" y="396">MGO100+</text>

      <!-- rating panel -->
      <line class="rating-rule" x1="300" y1="463" x2="628" y2="463" stroke="var(--rule)" stroke-width="1"/>
      <rect class="rating-panel" x="300" y="480" width="330" height="56" fill="var(--rating-cream)"/>
      <line class="rating-base" x1="300" y1="538" x2="630" y2="538" stroke="var(--rule)" stroke-width="1"/>
      <line class="rating-divider" x1="470" y1="476" x2="470" y2="524" stroke="var(--ink)" stroke-width="1"/>
      <text class="rating-value" x="385" y="515" text-anchor="middle">20+</text>
      <text class="rating-value" x="552" y="515" text-anchor="middle">514+</text>

      <text class="net-weight" x="468" y="562" text-anchor="middle">250mg | 8.0 oz</text>
    </svg>
  </section>
</main>
</body>
</html>
```